Capability Statement Brochure - Corporate

We need to provide our corporate clients with an elegant, professional and well designed capability statement that not only details what our business can offer, but reflects our professionalism with relevant technical photos. I am thinking two pages A 4 pdf will be suitable if the text can fit without looking crowded but happy to extend to 3 or 4 pages if needed . Colours and details can be taken from our website www.quorintech.com.au Some photos have been attached however if we need more professional stock photos I am happy to use them if needed. This project needs to convince potential clients we are the best in industry and our capability is extensive. Please help us relay this to our customers. Thank you,.

Target Market(s)

Corporate, Government, Education, Defence, Healthcare

Industry/Entity Type

Audio Visual Integration

Colors
0054AA
0677BA
7BADD7
CADEEF
E8F1F8

Requirements
Must have
• Style, look classy, sophisticated and technical
Nice to have
• Quorin Tech colours, Logo, website and email and include the PRISM LED Logo
Should not have
• Messy, too much clutter, not easy to read.

```html
<!DOCTYPE html>
<html lang="en">
<head>
<meta charset="utf-8">
<title>Quorin Tech Systems – Capability Statement</title>
<link rel="stylesheet" href="https://fonts.googleapis.com/css2?family=Montserrat:wght@500;700&family=Open+Sans:wght@400;600;700&display=swap">
<style>
:root{
  --blue-deep:#0054AA;
  --blue:#0677BA;
  --blue-mid:#7BADD7;
  --blue-pale:#CADEEF;
  --blue-mist:#E8F1F8;
  --orange:#E8731E;
  --ink:#3a4350;
  --paper:#ffffff;
  --backdrop:#e6e8eb;
}
*{margin:0;padding:0;box-sizing:border-box}
html,body{width:833px;height:1200px;overflow:hidden}
body{background:var(--backdrop);font-family:"Open Sans",Arial,sans-serif;color:var(--ink);position:relative}
.spread{position:absolute;left:36px;width:760px;height:520px;display:flex;box-shadow:0 2px 8px rgba(0,0,0,.12)}
.spread--cover{top:40px}
.spread--inside{top:640px}
.page{position:relative;width:380px;height:520px;background:var(--paper);overflow:hidden}
.page + .page{border-left:1px solid #dde3ea}
.photo{position:absolute}
.shape{position:absolute;left:0;top:0}
.footer-band{position:absolute;left:0;right:0;bottom:0;height:22px;background:var(--blue-deep);border-top:5px solid var(--orange)}
.footer-band span{position:absolute;right:16px;top:2px;font-size:9px;color:#fff;letter-spacing:.3px}
.heading{font-family:"Montserrat",Arial,sans-serif;font-weight:700;font-size:10px;color:var(--blue-deep);margin-bottom:4px}
.copy{font-size:7.5px;line-height:1.45}
ul.ticks{list-style:none;font-size:7.5px;line-height:1.7}
ul.ticks li::before{content:"";display:inline-block;width:5px;height:5px;background:var(--orange);margin-right:6px;vertical-align:1px}
.panel-blue{position:absolute;background:var(--blue);color:#fff;padding:10px 12px}
.panel-blue .heading{color:#fff;background:var(--orange);margin:-10px -12px 8px;padding:5px 12px}
.brand{position:absolute;display:flex;align-items:center;gap:7px;font-family:"Montserrat",Arial,sans-serif;font-weight:700;font-size:11px;color:var(--blue-deep)}
.brand i{width:14px;height:14px;background:var(--blue-deep);display:block}
.title-block{position:absolute;left:22px;top:78px;color:#fff}
.title-block small{display:block;font-family:"Montserrat",Arial,sans-serif;font-weight:500;font-size:9px;margin-bottom:6px;color:var(--blue-pale)}
.title-block h1{font-family:"Montserrat",Arial,sans-serif;font-weight:700;font-size:21px;line-height:1.15}
.text-block{position:absolute}
.icon-row{position:absolute;left:14px;right:14px;top:196px;display:flex;justify-content:space-between}
.icon-row figure{width:50px;text-align:center;font-size:7px;font-weight:600;color:var(--blue-deep)}
.icon-row svg{display:block;margin:0 auto 3px}
.card{position:absolute;width:168px}
.card .heading{background:var(--blue-deep);color:#fff;padding:4px 8px;font-size:8.5px}
</style>
</head>
<body>

<section class="spread spread--cover">
  <article class="page page--back">
    <div class="photo" role="img" aria-label="Photo of a tiered lecture theatre with projection screen" style="left:0;top:0;width:380px;height:200px;background:linear-gradient(160deg,#8a96a6,#3f4a5a 60%,#6f7b8c)"></div>
    <svg class="shape" width="380" height="206" viewBox="0 0 380 206"><polygon points="0,110 170,200 0,200" fill="#0054AA"/><rect x="0" y="200" width="380" height="6" fill="#E8731E"/></svg>
    <div class="text-block" style="left:20px;top:218px;width:150px">
      <p class="heading">Who We Are</p>
      <p class="copy">We design, install and support integrated audio visual systems for organisations across Australia.</p>
    </div>
    <div class="panel-blue" style="left:186px;top:150px;width:172px">
      <p class="heading">Our Services</p>
      <ul class="ticks">
        <li>Audio visual design</li><li>System integration</li><li>Video conferencing</li>
        <li>Digital signage</li><li>Control systems</li><li>Ongoing support</li>
      </ul>
    </div>
    <div class="photo" role="img" aria-label="Photo of a control desk with monitors and conferencing equipment" style="left:20px;top:310px;width:160px;height:150px;background:linear-gradient(170deg,#c9ced6,#6c7684)"></div>
    <div class="brand" style="left:200px;top:380px;font-size:14px"><i style="background:var(--orange)"></i>PRISM LED</div>
    <p class="copy" style="position:absolute;left:221px;top:402px">Authorised display partner</p>
    <div class="footer-band"></div>
  </article>

  <article class="page page--front">
    <div class="brand" style="left:22px;top:20px"><i></i>Quorin Tech Systems</div>
    <div class="photo" role="img" aria-label="Photo of a modern boardroom with a long table and display" style="left:150px;top:40px;width:230px;height:170px;background:linear-gradient(150deg,#eef2f6,#a9b5c3 70%,#7f8c9c)"></div>
    <svg class="shape" width="380" height="230" viewBox="0 0 380 230"><polygon points="0,60 200,40 140,210 0,210" fill="#0054AA"/><polygon points="140,210 200,40 206,40 146,210" fill="#7BADD7"/><rect x="0" y="210" width="380" height="5" fill="#E8731E"/></svg>
    <div class="title-block"><small>Quorin Tech Systems</small><h1>Capability<br>Statement</h1></div>
    <div class="text-block" style="left:22px;top:232px;width:160px">
      <p class="heading">Company Overview</p>
      <p class="copy">Quorin Tech Systems delivers reliable, high quality audio visual solutions for corporate, government, education, defence and healthcare clients.</p>
    </div>
    <div class="panel-blue" style="left:198px;top:232px;width:160px;background:var(--blue-mist);color:var(--ink)">
      <p class="heading">Our Capabilities</p>
      <ul class="ticks">
        <li>Boardrooms and meeting spaces</li><li>Lecture theatres</li><li>Control rooms</li><li>Training facilities</li>
      </ul>
    </div>
    <div class="footer-band"><span>www.quorintech.com.au</span></div>
  </article>
</section>

<section class="spread spread--inside">
  <article class="page page--inside-left">
    <div class="photo" role="img" aria-label="Photo of a bright collaboration room with wall displays" style="left:0;top:0;width:380px;height:180px;background:linear-gradient(160deg,#dfe6ee,#93a3b6 65%,#5d6b7d)"></div>
    <svg class="shape" width="380" height="186" viewBox="0 0 380 186"><polygon points="170,0 380,0 380,180 120,180" fill="#0054AA" opacity=".92"/><rect x="0" y="180" width="380" height="5" fill="#E8731E"/></svg>
    <div class="text-block" style="left:190px;top:26px;width:170px;color:#fff">
      <p class="heading" style="color:#fff;font-size:12px">Why Quorin Tech</p>
      <p class="copy">Experienced engineers, certified technicians and a proven record of on time delivery.</p>
    </div>
    <div class="icon-row">
      <figure><svg width="34" height="34" viewBox="0 0 34 34"><circle cx="17" cy="17" r="16" fill="#0677BA"/><path d="M11 23l12-12M20 11h3v3" stroke="#fff" stroke-width="2" fill="none"/></svg>Design</figure>
      <figure><svg width="34" height="34" viewBox="0 0 34 34"><circle cx="17" cy="17" r="16" fill="#0677BA"/><path d="M11 17l4 4 8-8" stroke="#fff" stroke-width="2" fill="none"/></svg>Install</figure>
      <figure><svg width="34" height="34" viewBox="0 0 34 34"><circle cx="17" cy="17" r="16" fill="#0677BA"/><rect x="11" y="11" width="12" height="12" rx="2" stroke="#fff" stroke-width="2" fill="none"/></svg>Control</figure>
      <figure><svg width="34" height="34" viewBox="0 0 34 34"><circle cx="17" cy="17" r="16" fill="#0677BA"/><rect x="9" y="12" width="11" height="10" fill="#fff"/><path d="M20 15l5-3v10l-5-3z" fill="#fff"/></svg>Video</figure>
      <figure><svg width="34" height="34" viewBox="0 0 34 34"><circle cx="17" cy="17" r="16" fill="#0677BA"/><path d="M10 14h4l5-4v14l-5-4h-4z" fill="#fff"/><path d="M22 13a6 6 0 0 1 0 8" stroke="#fff" stroke-width="2" fill="none"/></svg>Audio</figure>
      <figure><svg width="34" height="34" viewBox="0 0 34 34"><circle cx="17" cy="17" r="16" fill="#0677BA"/><path d="M12 12c0-3 10-3 10 3s-5 4-5 6M17 24v1" stroke="#fff" stroke-width="2" fill="none"/></svg>Support</figure>
    </div>
    <div class="text-block" style="left:18px;top:262px;width:160px">
      <p class="heading">Design &amp; Consulting</p>
      <p class="copy">Tailored solutions planned around how your people work.</p>
    </div>
    <div class="text-block" style="left:18px;top:330px;width:160px">
      <p class="heading">Healthcare &amp; Education</p>
      <p class="copy">Clear, dependable systems for teaching and clinical spaces.</p>
    </div>
    <div class="photo" role="img" aria-label="Photo of a clinical laboratory with technical equipment" style="left:196px;top:258px;width:166px;height:200px;background:linear-gradient(165deg,#f1f4f7,#b8c5d3 60%,#7e90a5)"></div>
    <div class="footer-band"></div>
  </article>

  <article class="page page--inside-right">
    <div class="photo" role="img" aria-label="Photo of a long boardroom with city windows" style="left:0;top:0;width:380px;height:170px;background:linear-gradient(160deg,#cfd8e2,#6f8297 60%,#3e4c5e)"></div>
    <div style="position:absolute;left:0;right:0;top:170px;height:5px;background:var(--orange)"></div>
    <div class="card" style="left:16px;top:190px">
      <p class="heading">Corporate Boardrooms</p>
      <p class="copy">Seamless meetings with simple one touch control.</p>
    </div>
    <div class="photo" role="img" aria-label="Photo of a meeting room table with microphones" style="left:196px;top:190px;width:168px;height:100px;background:linear-gradient(150deg,#dde3ea,#8e9cad)"></div>
    <div class="card" style="left:196px;top:300px">
      <p class="heading">Government &amp; Defence</p>
      <p class="copy">Secure systems built to strict standards.</p>
    </div>
    <div class="photo" role="img" aria-label="Photo of a conference table with a video call display" style="left:16px;top:250px;width:168px;height:110px;background:linear-gradient(150deg,#c7d1dc,#64748a)"></div>
    <div class="card" style="left:16px;top:372px">
      <p class="heading">Video Conferencing</p>
      <p class="copy">Connect teams anywhere with crystal clear calls.</p>
    </div>
    <div class="card" style="left:196px;top:372px">
      <p class="heading">Maintenance &amp; Support</p>
      <p class="copy">Responsive service to keep every room running.</p>
    </div>
    <div class="footer-band"><span>www.quorintech.com.au</span></div>
  </article>
</section>

</body>
</html>
```